Bar Wanderlust VIP Card design

Looking for a design for a VIP card forguests wishing to purchase to avoid cover charges, skipping the line and othe advantages.

We used our logo on last years card.I've also attached a few of our previous cards. Looking for something fresh.

We are not apposed to a vertical card either way would be fine We will have to incorporate the kelp fizz logo on the card as well.

Industry/Entity Type

Bar Restaurant www.tavern-quillo.example

Font styles to use
Decorative

```html
<!DOCTYPE html>
<html lang="en">
<head>
<meta charset="utf-8">
<title>Bar Wanderlust VIP Card 2023</title>
<link rel="stylesheet" href="https://fonts.googleapis.com/css2?family=Libre+Bodoni:wght@700&display=swap">
<style>
  :root {
    --page-bg: #e8e8e8;
    --card-black: #000000;
    --grey-dark: #2a2a2a;
    --grey-light: #8a8a8a;
    --olive: #cccc33;
    --bright-yellow: #ffff66;
    --marker-yellow: #cfd14a;
    --white: #ffffff;
    --badge-teal: #3d6868;
    --name-cream: #f3ec9e;
  }
  html, body {
    margin: 0;
    padding: 0;
    width: 1200px;
    height: 1000px;
    overflow: hidden;
    background: var(--page-bg);
  }
  .vip-card {
    position: absolute;
    left: 57px;
    top: 33px;
    width: 1095px;
    height: 627px;
    margin: 0;
    border-radius: 30px;
    overflow: hidden;
    background: var(--card-black);
    font-family: "Libre Bodoni", "Times New Roman", serif;
  }
  .vip-card__wave-area {
    position: absolute;
    left: 230px;
    top: 0;
    right: 0;
    bottom: 0;
    background: linear-gradient(200deg,
      var(--grey-light) 0%,
      var(--grey-dark) 38%,
      var(--olive) 62%,
      var(--bright-yellow) 80%,
      var(--grey-dark) 100%);
    -webkit-mask-image: linear-gradient(to right, transparent 0%, #000 45%);
    mask-image: linear-gradient(to right, transparent 0%, #000 45%);
  }
  .venue-mark {
    position: absolute;
    left: 30px;
    top: 80px;
    display: flex;
    align-items: center;
    gap: 12px;
  }
  .venue-mark__dot {
    width: 44px;
    height: 44px;
    border-radius: 50%;
    background: var(--badge-teal);
  }
  .venue-mark__name {
    color: var(--name-cream);
    font-size: 24px;
    font-weight: 700;
    letter-spacing: 0.5px;
    text-transform: uppercase;
  }
  .vip-title {
    position: absolute;
    right: 78px;
    top: 40px;
    width: 262px;
    margin: 0;
    text-align center;
    text-align: center;
    color: var(--white);
    font-weight: 700;
  }
  .vip-title__word {
    display: block;
    font-size: 140px;
    line-height: 1;
    letter-spacing: -3px;
  }
  .vip-title__marker {
    display: block;
    margin: 8px auto 0;
    width: 236px;
    height: 18px;
  }
  .vip-title__year {
    display: block;
    margin-top: 18px;
    font-size: 72px;
    line-height: 1;
  }
  .partner-mark {
    position: absolute;
    left: 62px;
    top: 500px;
    display: flex;
    align-items: center;
    gap: 12px;
    color: var(--white);
  }
  .partner-mark__square {
    width: 14px;
    height: 14px;
    background: var(--white);
  }
  .partner-mark__name {
    font-size: 26px;
    font-weight: 700;
    line-height: 1.2;
    text-transform: uppercase;
    text-align: center;
  }
</style>
</head>
<body>
  <main class="vip-card" aria-label="Bar Wanderlust VIP card 2023">
    <div class="vip-card__wave-area" role="img" aria-label="Flowing yellow and grey wave graphic across the card"></div>

    <div class="venue-mark">
      <span class="venue-mark__dot"></span>
      <span class="venue-mark__name">Bar Wanderlust</span>
    </div>

    <h1 class="vip-title">
      <span class="vip-title__word">VIP</span>
      <svg class="vip-title__marker" viewBox="0 0 236 18" aria-hidden="true">
        <polygon points="0,0 236,0 70,18" fill="var(--marker-yellow)"/>
      </svg>
      <span class="vip-title__year">2023</span>
    </h1>

    <div class="partner-mark">
      <span class="partner-mark__square"></span>
      <span class="partner-mark__name">Kelp<br>Fizz</span>
    </div>
  </main>
</body>
</html>
```